Music CD Design Project - 4 panel

Pop rock / soft rock ballad single CD case artwork.
Female singer in her 20s.
Would like something clean, classic, cool, sexy.

4 panel gatefold card case - Template: http://www.duplimark.com.au/storage/duplimark-artwork-templates/Duplimark%20Gatefold%20Sleeve.pdf

Artwork specifications:
http://www.duplimark.com.au/artwork-cd-dvd-replication/

Target Market(s)

Record Labels & Commercial Radio Stations / Listeners

Industry/Entity Type

Singer

Requirements
Must have
• Must have all 4 panels utilised (Template: http://www.duplimark.com.au/storage/duplimark-artwork-templates/Duplimark%20Gatefold%20Sleeve.pdf )
Must have text included (below) :
_______________________________________________________
COVER TEXT
ROS KERROW
Hollowed

INSIDE TEXT

HOLLOWED
Performed by: Rosalind Kerrow
Written By: Rosalind Kerrow, Gregory J. Olsen, Hugh Lamb
Recorded in Sydney NSW, produced, engineered and mixed by Gregory J. Olsen. Drums: Laurent Vischorelle. Vocals recorded at Tidal Studio, Perth WA.

PAINTED RIVERS
Written By: Rosalind Kerrow, Gregory J. Olsen
Produced and Mixed: Gregory Olsen at Gregory Olsen Studio, Sydney, New South Wales. Drums: Laurent Vischorelle.

BACK TEXT
Track 1: Hollowed
Track 2: Hollowed [Radio Edit]
Track 3: Painted Rivers

www.RosKerrowMusic.com
Photography: Rosalind Ivy Photography / Bree Vantorre Photography
_____________________________________________________
I have attached photos please use whatever you think will suit.
Inside text can be small print, I just need it there but doesn't have to be the feature / main item.
Nice to have
• LYRICS

HOLLOWED
You're in my picture frame / In black and white before the night you went away / I can't forget that day / My heart I heart it break / Like glass it fell and shattered silently / Your words cut violently / Left me to bleed / Stripped bare of my innocence / Your scent lingers on me / Sounds of an ambulance as my heart it screams / I wished for a nightmare / I prayed for the sun / Not even its warmth could heal me / And it's HOLLOWED to wish upon a star / HOLLOWED to wonder where you are / HOLLOWED I gotta change my tune / It's HOLLOWED I'm not wasting my time on you / Here comes another moon / Tell me how many nights did I cry for you / These tears of truth / Sunrise to sunsets I still remain / A prisoner to my bed for days, afraid / Because life is a maze without you / I taste the tears along my lips / Stuck in this solar eclipse / The day will end without my best friend / I wished for a nightmare / I prayed for the sun / Not even its warmth could heal me / And it's HOLLOWED to wish upon a star / HOLLOWED to wonder where you are / HOLLOWED I gotta change my tune / It's HOLLOWED I'm not wasting my time on you / Here comes another moon / Tell me how many nights did I cry for you / These tears of truth / Sunrise to sunsets I still remain / A prisoner to my bed for days, afraid / Because life is a maze without you / And it's HOLLOWED to wish upon a star / HOLLOWED to wonder where you are / HOLLOWED I gotta change my tune / It's HOLLOWED I'm not wasting my time on you.

PAINTED RIVERS
Hello Pinnochio, your other woman called / So cut your nose to spite your face / Your double mask will be defaced / Lying through your wooden teeth / Your puppet pants on fire / There's no real man underneath / You're one IMPRESSIVE LIAR / You think I'm blind, but I have eyes / I see right through your PAINTED RIVERS / The faith I had has now expired / Thrown out with your porky pies / This time I can't ignore I won't take it anymore / I'm calling your bluff cos I've had enough of your PAINTED RIVERS/ You're running late again, repeating that same old story / Improvisation of fiction, your compulsive addiction / Does nothing for me / Lost in a labyrinth of lies / Your tangled web on fire / Remembering every alibi / You're one IMPRESSIVE LIAR / You think I'm blind, but I have eyes / I see right through your PAINTED RIVERS / The faith I had has now expired / Thrown out with your porky pies / This time I can't ignore I won't take it anymore / I'm calling your bluff cos I've had enough of your PAINTED RIVERS / Words thrown around a thousand times / Promises are made and tossed aside / You think I'm wrapped around your finger / But I'm leaving you behind / You think I'm blind, but I have eyes / I see right through your PAINTED RIVERS / The faith I had has now expired / Thrown out with your porky pies / This time I can't ignore I won't take it anymore / I'm calling your bluff cos I've had enough of your IMPRESSIVE / I'm calling your bluff cos I've had enough of your PAINTED RIVERS

```html
<!DOCTYPE html>
<html lang="en">
<head>
<meta charset="utf-8">
<title>Ros Kerrow – Hollowed – Gatefold Sleeve Inside Spread</title>
<link href="https://fonts.googleapis.com/css2?family=Source+Sans+3:ital,wght@0,400;1,400&display=swap" rel="stylesheet">
<style>
  :root {
    --paper: #ffffff;
    --dieline: #555a55;
    --trim-mark: #d8d8d0;
    --ink-light: #f2f6ee;
    --sea-deep: #1d4f47;
    --sea-mid: #2f6e52;
    --grass: #4f9448;
    --grass-light: #7cb544;
  }
  html, body {
    margin: 0;
    padding: 0;
    width: 1200px;
    height: 1000px;
    overflow: hidden;
    background: var(--paper);
  }
  .sleeve {
    position: relative;
    width: 1200px;
    height: 1000px;
    font-family: "Source Sans 3", "Myriad Pro", sans-serif;
    color: var(--ink-light);
  }
  .sleeve__art {
    position: absolute;
    inset: 0;
  }
  .credits {
    position: absolute;
    left: 120px;
    top: 373px;
    font-size: 11px;
    line-height: 15.2px;
    letter-spacing: -0.1px;
    text-transform: uppercase;
    margin: 0;
  }
  .credits__song { margin: 0 0 15px; }
  .credits__title { font-style: italic; display: block; }
  .tracklist {
    position: absolute;
    left: 790px;
    width: 200px;
    top: 408px;
    margin: 0;
    padding: 0;
    list-style: none;
    text-align: center;
    font-size: 11px;
    line-height: 16px;
    text-transform: uppercase;
  }
  .back-footer {
    position: absolute;
    right: 6px;
    top: 704px;
    text-align: right;
    font-size: 7.5px;
    line-height: 18px;
    text-transform: uppercase;
  }
  .back-footer p { margin: 0; }
</style>
</head>
<body>
<main class="sleeve">
  <svg class="sleeve__art" width="1200" height="1000" viewBox="0 0 1200 1000">
    <defs>
      <linearGradient id="photo-tone" x1="0" y1="0" x2="0.25" y2="1">
        <stop offset="0" stop-color="#1f5248"/>
        <stop offset="0.3" stop-color="#2d6a4d"/>
        <stop offset="0.55" stop-color="#3f7f49"/>
        <stop offset="0.8" stop-color="#5a9a44"/>
        <stop offset="1" stop-color="#7ab848"/>
      </linearGradient>
      <radialGradient id="photo-glow" cx="0.2" cy="0.35" r="0.4">
        <stop offset="0" stop-color="#8fb848" stop-opacity="0.55"/>
        <stop offset="1" stop-color="#8fb848" stop-opacity="0"/>
      </radialGradient>
    </defs>

    <!-- trim marks -->
    <g class="trim-marks" stroke="var(--trim-mark)" stroke-width="1.5">
      <line x1="28" y1="0" x2="28" y2="18"/>
      <line x1="615" y1="0" x2="615" y2="18"/>
      <line x1="18" y1="890" x2="18" y2="948"/>
      <line x1="604" y1="890" x2="604" y2="948"/>
    </g>

    <!-- dieline of the pocket panel -->
    <path class="dieline" d="M620,142 L10,142 Q130,450 10,757 L620,757"
          fill="none" stroke="var(--dieline)" stroke-width="1.4" stroke-dasharray="5 4"/>

    <!-- photographic spread -->
    <g role="img" aria-label="Soft-focus photograph of green rolling ocean water with a wave line across the back panel">
      <path d="M30,155 L620,155 L660,52 L1150,52 L1200,150 L1200,745 L1150,848 L665,848 L620,745 L30,745 Q120,450 30,155 Z"
            fill="url(#photo-tone)"/>
      <path d="M30,155 L620,155 L660,52 L1150,52 L1200,150 L1200,745 L1150,848 L665,848 L620,745 L30,745 Q120,450 30,155 Z"
            fill="url(#photo-glow)"/>
    </g>
  </svg>

  <section class="credits" aria-label="Credits">
    <p class="credits__song">
      <span class="credits__title">Hollowed</span>
      Performed by: Rosalind Kerrow<br>
      Written by: Rosalind Kerrow, Gregory J. Olsen, Hugh Lamb<br>
      Recorded in Sydney NSW. Produced, engineered and mixed by Gregory J. Olsen.<br>
      Drums: Laurent Vischorelle. Vocals recorded at Tidal Studio, Perth WA.
    </p>
    <p class="credits__song">
      <span class="credits__title">Painted Rivers</span>
      Performed by: Rosalind Kerrow<br>
      Written by: Rosalind Kerrow, Gregory J. Olsen<br>
      Produced and mixed: Gregory Olsen at Gregory Olsen Studio, Sydney, New South<br>
      Wales. Drums: Laurent Vischorelle.
    </p>
  </section>

  <ol class="tracklist">
    <li>Track 1: Hollowed</li>
    <li>Track 2: Hollowed [Radio Edit]</li>
    <li>Track 3: Painted Rivers</li>
  </ol>

  <footer class="back-footer">
    <p>Photography: Rosalind Ivy Photography / Bree Vantorre Photography</p>
    <p>www.RosKerrowMusic.com</p>
  </footer>
</main>
</body>
</html>
```